The First Annual Fernwick Legacy Gala

Something similar to the attached but an attention grabber. It needs to attract people with money to spend!

```html
<!DOCTYPE html>
<html lang="en">
<head>
<meta charset="utf-8">
<title>The First Annual Fernwick Legacy Gala</title>
<link href="https://fonts.googleapis.com/css2?family=Arimo:wght@400;700&family=Lato:wght@400;700;900&display=swap" rel="stylesheet">
<style>
  :root {
    --blue: #5f8ac7;
    --blue-deep: #3f73c0;
    --blue-light: #82a6da;
    --blue-soft: #8fb1e3;
    --charcoal: #353535;
    --ink: #3b3b3b;
    --grey-swoosh: #d9d9d9;
    --white: #ffffff;
  }
  * { box-sizing: border-box; margin: 0; padding: 0; }
  html, body { width: 902px; height: 1200px; overflow: hidden; background: var(--white); }
  .flyer { position: relative; width: 902px; height: 1200px; overflow: hidden; font-family: "Lato", sans-serif; color: var(--ink); }
  .flyer-shapes { position: absolute; inset: 0; }
  .abs { position: absolute; }

  .presenter { top: 44px; left: 0; width: 902px; text-align: center; font-size: 21px; color: #1f2a3d; letter-spacing: .2px; }
  .event-title { top: 90px; left: 0; width: 902px; text-align: center; font-family: "Arimo", sans-serif; font-weight: 700; color: var(--white); font-size: 48px; line-height: 57px; }

  .event-date { left: 566px; top: 330px; font-family: "Arimo", sans-serif; font-weight: 700; color: var(--ink); }
  .event-date .month { font-size: 53px; line-height: 56px; }
  .event-date .year { font-size: 98px; line-height: 96px; letter-spacing: -1px; }
  .event-time { left: 566px; top: 490px; font-family: "Arimo", sans-serif; font-weight: 700; font-size: 19px; line-height: 25px; color: var(--ink); }
  .icon-clock { left: 512px; top: 494px; }
  .icon-glass { left: 808px; top: 492px; }

  .highlights { left: 38px; top: 648px; width: 360px; font-family: "Arimo", sans-serif; font-weight: 700; color: var(--blue-deep); font-size: 25px; line-height: 32px; }
  .details { left: 38px; top: 730px; width: 352px; font-size: 14.5px; line-height: 19.5px; color: #2e2e2e; }
  .details p + p { margin-top: 19px; }
  .details .short-gap { margin-top: 6px; line-height: 24px; }

  .follow { left: 40px; top: 1050px; width: 320px; text-align: center; font-size: 13.5px; line-height: 17px; font-weight: 700; color: #25324a; }
  .follow .org { color: var(--white); }

  .tickets-label { left: 480px; top: 632px; font-size: 19px; font-weight: 700; color: var(--blue-soft); }
  .icon-tickets { left: 480px; top: 668px; }
  .ticket-prices { left: 576px; top: 670px; color: var(--white); font-weight: 700; }
  .ticket-prices .amount { font-size: 33px; line-height: 42px; }
  .ticket-prices .unit { font-size: 19px; }
  .raffle-label { left: 426px; top: 779px; width: 476px; text-align: center; font-size: 19px; font-weight: 700; color: var(--blue-soft); }
  .raffle-price { left: 426px; top: 812px; width: 476px; text-align: center; font-size: 29px; font-weight: 700; color: var(--white); }
  .donor { left: 423px; top: 870px; width: 479px; text-align: center; font-size: 15px; line-height: 20px; font-weight: 700; color: #1f2a3d; }

  .outlets-title { left: 450px; top: 945px; font-size: 37px; font-weight: 700; color: var(--blue-soft); }
  .outlets { left: 455px; top: 1003px; width: 240px; font-size: 14px; line-height: 17px; color: var(--white); }
  .outlets li { list-style: none; margin-bottom: 10px; }
  .outlets strong { font-weight: 900; }
  .outlets-divider { left: 740px; top: 1006px; width: 1px; height: 95px; background: var(--blue-light); }
  .outlets-or { left: 731px; top: 1045px; width: 20px; text-align: center; font-size: 14px; color: var(--white); background: var(--charcoal); }
  .sellers { left: 762px; top: 1003px; font-size: 14px; line-height: 17px; color: var(--white); }
  .sellers .name { color: var(--blue-soft); font-weight: 700; margin-top: 11px; }
  .sellers .intro { font-weight: 700; }
</style>
</head>
<body>
<main class="flyer">
  <svg class="flyer-shapes" width="902" height="1200" viewBox="0 0 902 1200" aria-hidden="false">
    <rect width="902" height="1200" fill="var(--white)"/>
    <!-- header band -->
    <path d="M0 0 H902 V348 C720 280 430 232 0 268 Z" fill="var(--blue)"/>
    <path d="M0 268 C430 232 720 280 902 348 V358 C720 296 430 252 0 290 Z" fill="var(--grey-swoosh)"/>
    <!-- venue photo area -->
    <path d="M0 305 C180 275 400 262 580 270 L470 612 C300 618 150 600 0 588 Z" fill="url(#venueTones)" role="img" aria-label="Photo of the white community center building under a blue sky with a lawn in front"/>
    <path d="M0 566 C120 600 300 616 470 612 L466 622 C300 630 120 622 0 614 Z" fill="var(--blue)"/>
    <!-- dark ticket panel -->
    <path d="M423 1200 V640 C580 610 760 590 902 530 V1200 Z" fill="var(--charcoal)"/>
    <rect x="423" y="865" width="479" height="60" fill="var(--blue-light)"/>
    <!-- social bubble -->
    <ellipse cx="205" cy="1090" rx="235" ry="98" fill="var(--blue)"/>
    <circle cx="212" cy="1022" r="18" fill="var(--white)"/>
    <!-- bottom wave -->
    <path d="M0 1148 C300 1196 620 1160 902 1112 V1200 H0 Z" fill="var(--white)"/>
    <path d="M0 1162 C300 1206 620 1172 902 1124 V1200 H0 Z" fill="var(--blue)"/>
    <defs>
      <linearGradient id="venueTones" x1="0" y1="0" x2="0" y2="1">
        <stop offset="0" stop-color="#8fb6e6"/>
        <stop offset="0.45" stop-color="#e8eef4"/>
        <stop offset="0.62" stop-color="#c9cdc8"/>
        <stop offset="1" stop-color="#7f8a55"/>
      </linearGradient>
    </defs>
  </svg>

  <p class="abs presenter">THE FERNWICK COMMUNITY CENTER PRESENTS</p>
  <h1 class="abs event-title">THE FIRST ANNUAL<br>FERNWICK LEGACY GALA</h1>

  <div class="abs event-date">
    <div class="month">APRIL 23</div>
    <div class="year">2022</div>
  </div>
  <svg class="abs icon-clock" width="40" height="40" viewBox="0 0 40 40" aria-hidden="true">
    <rect x="2" y="2" width="36" height="36" rx="2" fill="none" stroke="var(--blue)" stroke-width="1.5"/>
    <circle cx="20" cy="20" r="12" fill="none" stroke="var(--blue)" stroke-width="1.2" stroke-dasharray="1.5 4"/>
    <path d="M20 11 V20 L26 24" fill="none" stroke="var(--blue)" stroke-width="1.8"/>
  </svg>
  <p class="abs event-time">STARTING AT 5:00 PM<br>WITH COCKTAIL HOUR</p>
  <svg class="abs icon-glass" width="34" height="42" viewBox="0 0 34 42" aria-hidden="true">
    <path d="M2 10 H32 L17 26 Z" fill="var(--blue)"/>
    <path d="M17 26 V38 M9 40 H25" stroke="var(--blue)" stroke-width="2.4"/>
    <path d="M24 2 L18 16" stroke="var(--blue)" stroke-width="1.6"/>
    <circle cx="23" cy="13" r="3" fill="var(--white)" stroke="var(--blue)" stroke-width="1"/>
  </svg>

  <h2 class="abs highlights">Live auction, silent auction,<br>raffle and a cash bar!</h2>
  <div class="abs details">
    <p>Come on out to the Fernwick Community Center for a delicious prime rib dinner, drinks, entertainment and more! There will be plenty of amazing auction items for everyone to choose from.</p>
    <p>All proceeds will go to the Fernwick Community Center. We will share some history of the school and each year we will highlight a local family. This year will be the Hartwell family who have been here for ....years!!</p>
    <p class="short-gap">High Side Barn, dirt bike, custom knives, a pack trip and so much more!</p>
  </div>

  <p class="abs follow">Follow the <span class="org">Fernwick Community Center's</span><br>Connectly page to see all the auction<br>items available!</p>

  <p class="abs tickets-label">TICKETS FOR THE EVENT ARE :</p>
  <svg class="abs icon-tickets" width="76" height="70" viewBox="0 0 76 70" aria-hidden="true">
    <rect x="6" y="4" width="60" height="32" rx="3" transform="rotate(-12 36 20)" fill="var(--blue)"/>
    <rect x="8" y="24" width="64" height="40" rx="3" fill="var(--blue)" stroke="var(--charcoal)" stroke-width="3"/>
    <rect x="18" y="33" width="44" height="22" fill="none" stroke="var(--charcoal)" stroke-width="2"/>
  </svg>
  <div class="abs ticket-prices">
    <div class="amount">$50 <span class="unit">EACH OR</span></div>
    <div class="amount">$90 <span class="unit">FOR A COUPLE</span></div>
  </div>
  <p class="abs raffle-label">TICKETS FOR THE 10X12 HIGH SIDE BARN</p>
  <p class="abs raffle-price">$25 EACH OR 5 FOR $100.</p>
  <p class="abs donor">DONATED BY:<br>RIDGELINE SHED WORKS OF ALDERBROOK, VALUE $6500</p>

  <h2 class="abs outlets-title">Get your tickets from:</h2>
  <ul class="abs outlets">
    <li><strong>Ridgeline Shed Works in Alderbrook</strong><br>42 Quarry Rd, Alderbrook</li>
    <li><strong>Summit Crest Realty</strong><br>218 W Birch St, Alderbrook</li>
    <li><strong>Fernwick Mercantile</strong><br>6120 County Road 14, Fernwick</li>
  </ul>
  <div class="abs outlets-divider"></div>
  <p class="abs outlets-or">or</p>
  <div class="abs sellers">
    <p class="intro">Get them from</p>
    <p class="name">Dana Corliss</p>
    <p>(555)014-2268</p>
    <p class="name">Jo Ellery</p>
    <p>(555)017-3391</p>
  </div>
</main>
</body>
</html>
```